依頼詳細
12月の年末繁忙期に合わせて、新聞折込を実施する予定です。ただ、おコメの麺の説明が難しく消費者には伝わりにくいため、純粋にちゃんぽんや台湾風まぜそばを全面に打ち出して当社に来店してもらい、結果的に米粉麺だったくらいの主張でいいと思っています。チラシの下部に100円キャッシュバック券をつけたいと考えています。(期限は2023年2月末)
記載項目
こむぎ茶屋 しずくや みずほ灯籠館店 (道の駅みずほ灯籠館内フードコート)
住所 長岡市桜井町318 TEL090-6978-5739
営業時間10:00~19:00

とろみちゃんぽん 880円
とろみちゃんぽん旨辛味噌のせ 910円
台湾風まぜそば 910円
サイズ
A4
ページ数
片面
希望イメージ
シンプル 複雑
単色 カラフル
暗い 明るい
日常 高級
遊び心 厳粛
未来的 伝統的
女性的 男性的
希望する色
黄・オレンジ系
納品ファイル
• 高解像度JPG (.jpg)

はじめてみた人が感じるインパクトがあり、色彩もよかったです。

毎回たくさんの応募ありがとうございます。
結果的に非常に満足しておりますので、これからも依頼したいと思います。
よろしくお願いします。

```html
<!DOCTYPE html>
<html lang="ja">
<head>
<meta charset="utf-8">
<title>こむぎ茶屋 しずくや 折込チラシ</title>
<link href="https://fonts.googleapis.com/css2?family=Noto+Sans+JP:wght@500;700;900&family=Noto+Serif+JP:wght@700;900&display=swap" rel="stylesheet">
<style>
  :root {
    --orange: #f39a1f;
    --orange-deep: #e5760c;
    --ink: #231815;
    --white: #ffffff;
    --cream: #efe4cf;
    --red: #d7261e;
    --yellow: #fdd23c;
    --brown: #6b4326;
  }
  * { margin: 0; padding: 0; box-sizing: border-box; }
  html, body { width: 847px; height: 1200px; overflow: hidden; }
  body { font-family: "Noto Sans JP", sans-serif; color: var(--ink); }
  .flyer {
    position: relative; width: 847px; height: 1200px; overflow: hidden;
    background: linear-gradient(180deg, var(--orange) 0%, var(--orange-deep) 100%);
  }
  .header {
    position: absolute; left: 0; top: 0; width: 847px; height: 104px;
    background: var(--white);
  }
  .header-mark {
    position: absolute; left: 22px; top: 16px; width: 72px; height: 72px;
    border-radius: 50%; background: var(--ink);
  }
  .header-lead, .header-shop {
    position: absolute; left: 112px; font-family: "Noto Serif JP", serif; font-weight: 900; white-space: nowrap;
  }
  .header-lead { top: 10px; font-size: 32px; }
  .header-shop { top: 52px; font-size: 36px; }
  .intro {
    position: absolute; left: 30px; top: 124px; color: var(--white);
    font-family: "Noto Serif JP", serif; font-weight: 900; font-size: 33px; line-height: 1.3;
  }
  .catch {
    position: absolute; font-family: "Noto Serif JP", serif; font-weight: 900; white-space: nowrap; line-height: 1;
    paint-order: stroke fill;
  }
  .catch-smooth {
    left: 280px; top: 124px; font-size: 124px; color: var(--white); letter-spacing: 2px;
    -webkit-text-stroke: 10px var(--ink);
  }
  .catch-chewy, .catch-throat {
    left: 22px; font-size: 106px; color: var(--ink); letter-spacing: 1px;
    -webkit-text-stroke: 8px var(--white);
  }
  .catch-chewy { top: 262px; }
  .catch-throat { top: 380px; }
  .photo { position: absolute; }
  .photo-champon {
    left: 388px; top: 478px; width: 459px; height: 430px;
    border-radius: 46% 0 0 50% / 50% 0 0 50%;
    background: linear-gradient(150deg, #f6efe2 0%, var(--cream) 45%, #d9c7a6 80%, #3a2f28 100%);
  }
  .photo-spicy {
    left: 0; top: 548px; width: 300px; height: 200px;
    border-radius: 0 50% 45% 0 / 0 50% 50% 0;
    background: linear-gradient(160deg, #f2e6cc 0%, #e3a368 55%, #8a4a26 100%);
  }
  .photo-mazesoba {
    left: 0; top: 770px; width: 400px; height: 430px;
    border-radius: 0 50% 0 0 / 0 48% 0 0;
    background: linear-gradient(170deg, #8c5a33 0%, var(--brown) 45%, #2e241d 100%);
  }
  .price {
    position: absolute; font-family: "Noto Serif JP", serif; font-weight: 900; white-space: nowrap; line-height: 1.1;
    color: var(--yellow); paint-order: stroke fill; -webkit-text-stroke: 5px var(--ink);
  }
  .price small { font-size: 21px; }
  .price b { font-size: 44px; }
  .price-spicy { left: 14px; top: 738px; }
  .price-champon { left: 650px; top: 866px; text-align: right; }
  .price-mazesoba { left: 24px; top: 1136px; }
  .shop-info { position: absolute; left: 418px; top: 930px; font-weight: 700; line-height: 1.3; color: var(--ink); }
  .shop-info .name { font-size: 22px; font-weight: 900; }
  .shop-info .note { font-size: 12px; }
  .shop-info .line { font-size: 14px; }
  .shop-info .hours { font-size: 19px; font-weight: 900; }
  .shop-info .tel { font-size: 22px; font-weight: 900; display: flex; align-items: center; gap: 6px; }
  .coupon {
    position: absolute; left: 416px; top: 1092px; width: 416px;
    background: var(--yellow); border: 3px dashed var(--ink); text-align: center; padding-bottom: 3px;
  }
  .coupon-head { background: var(--white); color: var(--ink); font-weight: 900; font-size: 16px; line-height: 1.5; }
  .coupon-value { color: var(--red); font-family: "Noto Serif JP", serif; font-weight: 900; font-size: 36px; line-height: 1.15; }
  .coupon-limit { font-size: 11px; font-weight: 700; line-height: 1.4; }
</style>
</head>
<body>
<main class="flyer">
  <header class="header">
    <div class="header-mark"></div>
    <p class="header-lead">道の駅みずほ灯籠館のフードコートにある</p>
    <p class="header-shop">こむぎ茶屋「しずくや」です。</p>
  </header>

  <p class="intro">新潟産米を使用<br>したお米の麺は、</p>
  <p class="catch catch-smooth">つるつる</p>
  <p class="catch catch-chewy">もちもち食感で</p>
  <p class="catch catch-throat">抜群ののど越し!</p>

  <div class="photo photo-champon" role="img" aria-label="白いスープのとろみちゃんぽんの写真"></div>
  <div class="photo photo-spicy" role="img" aria-label="旨辛味噌をのせたとろみちゃんぽんの写真"></div>
  <div class="photo photo-mazesoba" role="img" aria-label="卵黄とひき肉をのせた台湾風まぜそばの写真"></div>

  <p class="price price-spicy"><small>とろみちゃんぽん<br>旨辛味噌のせ</small><b>910</b><small>円</small></p>
  <p class="price price-champon"><small>とろみちゃんぽん</small><br><b>880</b><small>円</small></p>
  <p class="price price-mazesoba"><small>台湾風まぜそば</small><b>910</b><small>円</small></p>

  <section class="shop-info">
    <p class="name">こむぎ茶屋しずくや<br>みずほ灯籠館店</p>
    <p class="note">(道の駅みずほ灯籠館内フードコート)</p>
    <p class="line">長岡市桜井町318</p>
    <p class="hours">営業時間10:00~19:00</p>
    <p class="tel">
      <svg width="20" height="20" viewBox="0 0 24 24" aria-hidden="true"><path fill="#231815" d="M6.6 10.8a15 15 0 0 0 6.6 6.6l2.2-2.2a1 1 0 0 1 1-.25 11.4 11.4 0 0 0 3.6.57 1 1 0 0 1 1 1V20a1 1 0 0 1-1 1A17 17 0 0 1 3 4a1 1 0 0 1 1-1h3.5a1 1 0 0 1 1 1c0 1.25.2 2.45.57 3.57a1 1 0 0 1-.25 1z"/></svg>
      090-4213-8062
    </p>
  </section>

  <section class="coupon">
    <p class="coupon-head">こむぎ茶屋「しずくや」</p>
    <p class="coupon-value">100円OFF券</p>
    <p class="coupon-limit">期限:2023年2月末</p>
  </section>
</main>
</body>
</html>
```